Sturdyflow Mechanical - Letterhead

We are a plumbing and hvac company based in Calgary. This letterhead will be on our quotes, invoices, preventative maintenance proposals etc.

```html
<!DOCTYPE html>
<html lang="en">
<head>
<meta charset="utf-8">
<title>Sturdyflow Mechanical – Letterhead</title>
<link href="https://fonts.googleapis.com/css2?family=Arimo:wght@400&family=Montserrat:wght@500;600;800&family=Nunito+Sans:wght@400;600&display=swap" rel="stylesheet">
<style>
  :root{
    --stage-dark:#6c6c6c;
    --stage-light:#a9a9a9;
    --paper:#ffffff;
    --paper-shade:#ebebec;
    --paper-two:#f2f2f2;
    --brand-blue:#1f6fc0;
    --brand-orange:#f0592a;
    --ink:#4a4a4a;
    --ink-soft:#555;
    --mark-tint:#f3ddd6;
    --label:#f4f4f4;
  }
  *{margin:0;padding:0;box-sizing:border-box}
  html,body{width:1200px;height:774px;overflow:hidden}
  body{
    position:relative;
    background:linear-gradient(100deg,var(--stage-dark) 0%,var(--stage-dark) 62%,var(--stage-light) 100%);
    font-family:"Arimo",Arial,sans-serif;
  }
  .sheet{
    position:absolute;top:61px;width:458px;height:643px;
    box-shadow:2px 2px 5px rgba(0,0,0,.35);
    overflow:hidden;
  }
  .sheet--letter{left:125px;background:linear-gradient(150deg,var(--paper) 0%,#f8f8f8 55%,var(--paper-shade) 100%)}
  .sheet--back{left:628px;background:var(--paper-two)}
  .backdrop-mark{position:absolute;left:88px;top:210px;width:284px;height:284px;border-radius:50%;background:var(--mark-tint);opacity:.55}
  .sheet--back .backdrop-mark{opacity:.75}

  .brand{position:absolute;left:40px;top:38px;display:flex;align-items:center;gap:6px}
  .brand__dot{width:14px;height:14px;border-radius:50%;background:var(--brand-orange);flex:none}
  .brand__name{font-family:"Montserrat",sans-serif;font-weight:800;font-size:13px;line-height:15px;color:var(--brand-blue);text-transform:uppercase;width:100px}

  .contact{position:absolute;left:307px;top:63px;list-style:none;font-family:"Nunito Sans",sans-serif;font-size:7.3px;color:var(--ink);line-height:9px}
  .contact li{display:flex;align-items:center;gap:4px}
  .contact svg{width:6px;height:6px;fill:var(--brand-blue);flex:none}

  .letter{position:absolute;left:40px;top:184px;width:379px;color:var(--ink-soft)}
  .letter__greeting{font-size:11.5px;margin-bottom:23px}
  .letter p{font-size:6.9px;line-height:9.8px;text-align:justify;margin-bottom:9.8px}
  .letter__closing{margin-top:12px;font-size:6.9px}
  .signature{display:block;margin-left:-3px;width:137px;height:36px;background:linear-gradient(90deg,rgba(40,40,40,.18),rgba(40,40,40,.08));border-radius:3px}

  .footer{position:absolute;left:0;right:0;top:605px;text-align:center;font-family:"Nunito Sans",sans-serif;font-size:7px;line-height:9px;color:var(--ink)}
  .footer__name{color:var(--brand-blue);font-weight:600}

  .page-label{position:absolute;top:717px;font-family:"Montserrat",sans-serif;font-weight:600;font-size:17px;color:var(--label);transform:translateX(-50%)}
</style>
</head>
<body>
  <section class="sheet sheet--letter">
    <div class="backdrop-mark" aria-hidden="true"></div>
    <div class="brand">
      <span class="brand__dot"></span>
      <span class="brand__name">Sturdyflow Mechanical Inc</span>
    </div>
    <ul class="contact">
      <li><svg viewBox="0 0 10 10"><path d="M2 0l2 2-1 1.5a6 6 0 0 0 3.5 3.5L8 6l2 2-1.5 2C4 10 0 6 0 1.5z"/></svg>403-555-0148</li>
      <li><svg viewBox="0 0 10 10"><path d="M2.5 0h5v10h-5zM3.5 1v7h3V1z"/></svg>403-555-0192</li>
      <li><svg viewBox="0 0 10 10"><path d="M0 2h10v6H0zM1 3l4 3 4-3z"/></svg>info@sturdyflowmechanical.com</li>
      <li><svg viewBox="0 0 10 10"><circle cx="5" cy="5" r="5"/></svg>www.sturdyflowmechanical.com</li>
    </ul>

    <article class="letter">
      <h1 class="letter__greeting" style="font-weight:400">Dear Mr. Dalton,</h1>
      <p>Lorem ipsum dolor sit amet, consectetur adipiscing elit. Donec orci purus, luctus vitae dignissim eu, iaculis sed purus. Vivamus faucibus, ipsum nec aliquet viverra, leo mauris condimentum ligula, sit amet sagittis enim ligula quis arcu. Nam egestas tortor id nisi porttitor mattis. In tortor ante, ultricies in suscipit a, tempus non massa. Vivamus et auctor mi. Fusce vel massa nulla. Phasellus nec eros mauris, et scelerisque orci.</p>
      <p>Donec malesuada orci vitae nulla accumsan porta a id massa. Quisque accumsan iaculis magna sit amet fringilla. Maecenas consequat, magna eget tincidunt semper, odio nibh rutrum mi, id feugiat ante nisi eu risus. Vestibulum nunc orci, rhoncus a placerat in, ultricies in mi. Cras mattis varius eros, vel fringilla nisi suscipit eget. Quisque scelerisque sagittis nulla at porttitor.</p>
      <p>Sed id augue vitae urna euismod commodo aliquet a quam. Pellentesque arcu velit, cursus et malesuada ut, consequat et diam. Nullam erat sem, rhoncus id ullamcorper vitae, rhoncus et arcu. In ultricies ultricies nulla, ut rutrum nisi iaculis at. Donec eu magna a metus ornare faucibus. Fusce aliquet faucibus ultricies. Morbi semper, est id tincidunt gravida, sem arcu adipiscing lacus, ac bibendum nulla leo eu purus. Quisque nec diam sed risus consectetur a ccumsan quis quis nibh. Vestibulum id purus lorem.</p>
      <p>It is a long established fact that a reader will be distracted by the readable content of a page when looking at its layout. The point of using Lorem Ipsum is that it has a more-or-less normal distribution of letters, as opposed to using 'Content here, content here', making it look like readable English. Many desktop publishing packages</p>
      <p>ada ut, consequat et diam. Nullam erat sem, rhoncus id ullamcorper vitae, rhoncus et arcu. In ultricies ultricies nulla, ut rutrum nisi iaculis at. Donec eu magna a metus ornare faucibus. Fusce aliquet faucibus ultricies. Morbi semper,</p>
      <div class="letter__closing">Sincerely,</div>
      <span class="signature" role="img" aria-label="Handwritten signature of the sender"></span>
    </article>

    <footer class="footer">
      <div class="footer__name">Sturdyflow Mechanical Inc</div>
      <div>2140 Larkspur Way, Calgary, Alberta T2E 4K9</div>
    </footer>
  </section>

  <section class="sheet sheet--back">
    <div class="backdrop-mark" aria-hidden="true"></div>
  </section>

  <div class="page-label" style="left:357px">Page_01</div>
  <div class="page-label" style="left:855px">Page_02</div>
</body>
</html>
```